Flyer Design - Brenner Lindqvist AG

I’d like to redesign an A5, double-sided flyer for the company Brenner Lindqvist AG (https://www.blindqvist-example.ch/Home.htm). The text/content is available in a Word document.

```html
<!DOCTYPE html>
<html lang="de">
<head>
<meta charset="utf-8">
<title>Brenner Lindqvist AG – Flyer</title>
<link href="https://fonts.googleapis.com/css2?family=Montserrat:wght@400;500;600;700;800&display=swap" rel="stylesheet">
<style>
:root{
  --navy:#1f2f55;
  --red:#e3222b;
  --blue:#1f7fc1;
  --grey:#e6e8ec;
  --muted:#555b66;
  --stage:#3a3a3a;
  --white:#ffffff;
}
*{margin:0;padding:0;box-sizing:border-box}
html,body{width:692px;height:1200px;overflow:hidden}
body{background:var(--stage);font-family:'Montserrat',sans-serif;color:var(--navy);position:relative}
.page{position:absolute;left:146px;width:400px;height:568px;background:var(--white);overflow:hidden}
.page--front{top:24px}
.page--back{top:608px}
.abs{position:absolute}

/* front */
.front-header{left:0;top:0;width:400px;height:75px;background:var(--navy)}
.brand{left:0;top:0;width:400px;height:75px;display:flex;align-items:center;justify-content:center;gap:8px}
.brand-mark{width:14px;height:14px;background:var(--blue)}
.brand-name{color:var(--white);font-weight:700;font-size:17px;letter-spacing:.3px}
.brand-rule{left:0;top:75px;width:400px;height:3px;background:var(--red)}
.hero{left:0;top:78px;width:400px;height:162px}
.hero-title{left:17px;top:94px;color:var(--white);font-weight:800;font-size:25px;line-height:33px;letter-spacing:.3px}
.tagline{left:0;top:240px;width:400px;height:54px;background:var(--white);text-align:center}
.tagline h2{margin-top:11px;font-weight:700;font-size:16.5px;letter-spacing:.4px}
.tagline p{margin-top:4px;font-size:9.6px;color:var(--red);font-weight:500}
.services{left:0;top:294px;width:400px;height:128px;background:var(--grey)}
.services-divider{left:199px;top:305px;width:1px;height:110px;background:#9aa4b8}
.service{position:absolute;display:flex;align-items:center;gap:8px}
.service svg{flex:none}
.service b{display:block;font-size:9.4px;font-weight:700;line-height:10px}
.service span{display:block;font-size:7.6px;color:var(--muted);margin-top:1px}
.solar-photo{left:0;top:422px;width:400px;height:104px;background:linear-gradient(160deg,#8fa7b8 0%,#4e5e7a 45%,#6d8a55 100%)}
.footer-red{left:0;top:526px;width:400px;height:20px;background:var(--red);color:var(--white)}
.footer-navy{left:0;top:546px;width:400px;height:22px;background:var(--navy);color:var(--white)}
.contact{position:absolute;display:flex;align-items:center;gap:4px;font-size:8.4px;font-weight:500;white-space:nowrap}
.contact--phone{font-size:14px;font-weight:700}

/* back */
.back-header{left:0;top:0;width:400px;height:128px;background:var(--navy)}
.back-title{left:18px;top:18px;color:var(--white);font-weight:800;font-size:21.5px;line-height:27px;letter-spacing:.3px}
.since{left:18px;top:103px;color:var(--white);font-size:10.8px}
.since em{font-style:normal;color:var(--red);font-weight:700}
.intro{left:18px;top:136px;width:245px;color:var(--red);font-size:8.7px;line-height:11px;font-weight:500}
.checklist{left:18px;top:164px;width:200px;list-style:none}
.checklist li{margin-bottom:6px;padding-left:12px;position:relative}
.checklist li svg{position:absolute;left:0;top:1px}
.checklist b{display:block;font-size:9.3px;font-weight:700;line-height:11px}
.checklist span{display:block;font-size:7.4px;color:var(--muted);line-height:9px;width:168px}
.service-area{left:0;top:353px;width:240px;height:173px;background:var(--grey)}
.packs{left:18px;top:360px;width:200px}
.packs h3{font-size:11.5px;color:var(--red);font-weight:600}
.packs p{font-size:7.5px;color:var(--muted);line-height:9px;margin-top:4px}
.packs h4{font-size:9.3px;font-weight:600;margin-top:9px}
.packs .detail{font-size:7.3px;line-height:10px;margin-top:3px}
.badge-ribbon{left:40px;top:473px;width:176px;height:28px}
.badge-text{left:76px;top:476px;color:var(--white);font-size:9.2px;font-weight:700;line-height:10.5px;white-space:nowrap}
.badge-circle{left:18px;top:466px;width:52px;height:52px;border-radius:50%;background:var(--white);border:3px solid var(--navy);display:flex;align-items:center;justify-content:center;font-weight:800;font-size:18px}
.badge-circle small{font-size:9px;margin-top:5px}
</style>
</head>
<body>

<section class="page page--front">
  <div class="abs front-header"></div>
  <div class="abs brand"><span class="brand-mark"></span><span class="brand-name">Brenner Lindqvist AG</span></div>
  <div class="abs brand-rule"></div>

  <svg class="abs hero" viewBox="0 0 400 162" role="img" aria-label="Photo of a roofer working on a roof, overlaid with a blue-to-red colour band">
    <defs>
      <linearGradient id="heroBand" x1="0" y1="0" x2="1" y2="0">
        <stop offset="0" stop-color="#1f7fc1"/>
        <stop offset="0.55" stop-color="#8a3a5c"/>
        <stop offset="1" stop-color="#e3222b"/>
      </linearGradient>
      <linearGradient id="heroPhoto" x1="0" y1="0" x2="1" y2="1">
        <stop offset="0" stop-color="#5d6f8f"/>
        <stop offset="1" stop-color="#2b3550"/>
      </linearGradient>
    </defs>
    <rect width="400" height="162" fill="url(#heroPhoto)"/>
    <polygon points="0,0 195,0 295,162 0,162" fill="url(#heroBand)"/>
  </svg>
  <h1 class="abs hero-title">SANITÄR<br>SPENGLEREI<br>FLACHDACH<br>SOLARENERGIE</h1>

  <div class="abs tagline">
    <h2>PLANUNG | BERATUNG | AUSFÜHRUNG</h2>
    <p>Für Privatkundschaft &amp; Verwaltungen – schnell, sauber, zuverlässig.</p>
  </div>

  <div class="abs services"></div>
  <div class="abs services-divider"></div>

  <div class="service" style="left:18px;top:308px">
    <svg width="28" height="24" viewBox="0 0 28 24"><rect x="2" y="10" width="24" height="9" rx="2" fill="#1f7fc1"/><rect x="4" y="3" width="3" height="8" fill="#1f2f55"/></svg>
    <div><b>BADUMBAU</b><span>Ihr Weg zum Traumbad</span></div>
  </div>
  <div class="service" style="left:18px;top:346px">
    <svg width="28" height="24" viewBox="0 0 28 24"><polygon points="2,14 18,4 26,10 10,20" fill="#1f7fc1"/></svg>
    <div><b>SPENGLERARBEITEN</b><span>Dach &amp; Fassade nach Mass</span></div>
  </div>
  <div class="service" style="left:18px;top:384px">
    <svg width="28" height="24" viewBox="0 0 28 24"><circle cx="12" cy="12" r="9" fill="none" stroke="#1f7fc1" stroke-width="2.5"/><path d="M8 9h8v6H8z" fill="#1f2f55"/></svg>
    <div><b>24H NOTDIENST</b><span>Schnell vor Ort</span></div>
  </div>
  <div class="service" style="left:218px;top:304px">
    <svg width="28" height="24" viewBox="0 0 28 24"><circle cx="9" cy="15" r="6" fill="#1f2f55"/><rect x="14" y="4" width="10" height="4" fill="#1f7fc1"/><circle cx="22" cy="17" r="3" fill="#1f7fc1"/></svg>
    <div><b>SANITÄR-SERVICE<br>&amp; Reparaturen</b><span>Reparaturen &amp; schnelle Hilfe</span></div>
  </div>
  <div class="service" style="left:218px;top:346px">
    <svg width="28" height="24" viewBox="0 0 28 24"><circle cx="14" cy="12" r="10" fill="none" stroke="#1f7fc1" stroke-width="2"/><rect x="8" y="7" width="12" height="10" fill="#1f2f55"/></svg>
    <div><b>FLACHDACH</b><span>Neubau | Sanierung | Abdichtung</span></div>
  </div>
  <div class="service" style="left:218px;top:384px">
    <svg width="28" height="24" viewBox="0 0 28 24"><rect x="3" y="9" width="20" height="13" fill="#1f7fc1"/><circle cx="14" cy="6" r="4" fill="#1f2f55"/></svg>
    <div><b>SERVICEPAKETE</b><span>Boiler | Filter | Dachwartung</span></div>
  </div>

  <div class="abs solar-photo" role="img" aria-label="Photo of a house roof fitted with solar panels in a green landscape"></div>

  <div class="abs footer-red">
    <div class="contact contact--phone" style="left:14px;top:2px">
      <svg width="8" height="8" viewBox="0 0 10 10"><circle cx="5" cy="5" r="5" fill="#fff"/><path d="M3 3l1.5 0 .5 1.5-1 .6a4 4 0 0 0 1.9 1.9l.6-1 1.5.5V8A5 5 0 0 1 3 3z" fill="#e3222b"/></svg>+41 41 555 20 40</div>
    <div class="contact" style="left:228px;top:5px">
      <svg width="7" height="7" viewBox="0 0 10 10"><circle cx="5" cy="5" r="5" fill="#fff"/><rect x="2.5" y="3.2" width="5" height="3.6" fill="#e3222b"/></svg>info@blindqvist-example.ch</div>
  </div>
  <div class="abs footer-navy">
    <div class="contact" style="left:14px;top:6px">
      <svg width="7" height="8" viewBox="0 0 10 12"><path d="M5 0a4.5 4.5 0 0 1 4.5 4.5C9.5 8 5 12 5 12S.5 8 .5 4.5A4.5 4.5 0 0 1 5 0z" fill="#fff"/><circle cx="5" cy="4.5" r="1.6" fill="#1f2f55"/></svg>Lindenweg 14, 4999 Musterdorf</div>
    <div class="contact" style="left:228px;top:6px">
      <svg width="7" height="7" viewBox="0 0 10 10"><circle cx="5" cy="5" r="4.3" fill="none" stroke="#fff" stroke-width="1.2"/><path d="M.7 5h8.6M5 .7c-2 2.5-2 6 0 8.6M5 .7c2 2.5 2 6 0 8.6" fill="none" stroke="#fff" stroke-width=".9"/></svg>www.blindqvist-example.ch</div>
  </div>
</section>

<section class="page page--back">
  <div class="abs back-header"></div>
  <h1 class="abs back-title">MEHR KOMFORT.<br>MEHR SICHERHEIT.<br>MEHR WERTERHALT.</h1>
  <p class="abs since"><em>Seit 1881</em> – traditionelles Handwerk und moderne Lösungen.</p>

  <svg class="abs" style="left:0;top:128px" width="400" height="398" viewBox="0 0 400 398" role="img" aria-label="Photos of a plumber fitting a washbasin and of a team discussing plans, framed by navy and red diagonal panels">
    <defs>
      <linearGradient id="photoTop" x1="0" y1="0" x2="1" y2="1">
        <stop offset="0" stop-color="#7b6a5c"/><stop offset="1" stop-color="#2f2a28"/>
      </linearGradient>
      <linearGradient id="photoBottom" x1="0" y1="0" x2="1" y2="1">
        <stop offset="0" stop-color="#e9e6e2"/><stop offset="1" stop-color="#8c8580"/>
      </linearGradient>
    </defs>
    <polygon points="295,0 400,0 400,225 205,225" fill="url(#photoTop)"/>
    <polygon points="205,225 400,225 400,398 280,398 230,330" fill="url(#photoBottom)"/>
    <polygon points="310,0 295,0 205,225 230,225" fill="#ffffff"/>
    <polygon points="400,110 400,300 345,225" fill="#e3222b"/>
    <polygon points="205,225 250,225 230,262" fill="#1f2f55"/>
    <polygon points="345,225 400,300 400,398 380,398" fill="#e3222b"/>
  </svg>

  <p class="abs intro">Wir unterstützen Sie von der Beratung bis zur Ausführung unkompliziert, sauber und zuverlässig:</p>
  <ul class="abs checklist">
    <li><svg width="8" height="8" viewBox="0 0 10 10"><circle cx="5" cy="5" r="4.2" fill="none" stroke="#e3222b" stroke-width="1.3"/><path d="M3 5l1.6 1.6L8 2.8" fill="none" stroke="#e3222b" stroke-width="1.4"/></svg><b>Badumbau &amp; Sanierungen</b><span>Ihr Weg zum Traumbad</span></li>
    <li><svg width="8" height="8" viewBox="0 0 10 10"><circle cx="5" cy="5" r="4.2" fill="none" stroke="#e3222b" stroke-width="1.3"/><path d="M3 5l1.6 1.6L8 2.8" fill="none" stroke="#e3222b" stroke-width="1.4"/></svg><b>Sanitär-Service &amp; Reparaturen</b><span style="width:190px">schnell vor Ort bei Störungen und Schäden</span></li>
    <li><svg width="8" height="8" viewBox="0 0 10 10"><circle cx="5" cy="5" r="4.2" fill="none" stroke="#e3222b" stroke-width="1.3"/><path d="M3 5l1.6 1.6L8 2.8" fill="none" stroke="#e3222b" stroke-width="1.4"/></svg><b>Boilerwartung &amp; Service</b><span style="width:190px">damit Warmwasser jederzeit funktioniert</span></li>
    <li><svg width="8" height="8" viewBox="0 0 10 10"><circle cx="5" cy="5" r="4.2" fill="none" stroke="#e3222b" stroke-width="1.3"/><path d="M3 5l1.6 1.6L8 2.8" fill="none" stroke="#e3222b" stroke-width="1.4"/></svg><b>Spenglerei rund um Dach &amp; Fassade</b><span>Dachrinnen, Anschlüsse, Einfassungen,<br>Metallarbeiten nach Mass</span></li>
    <li><svg width="8" height="8" viewBox="0 0 10 10"><circle cx="5" cy="5" r="4.2" fill="none" stroke="#e3222b" stroke-width="1.3"/><path d="M3 5l1.6 1.6L8 2.8" fill="none" stroke="#e3222b" stroke-width="1.4"/></svg><b>Flachdach</b><span>Neubau, Abdichtung, Sanierung sowie<br>Wartung für langfristige Dichtheit</span></li>
    <li><svg width="8" height="8" viewBox="0 0 10 10"><circle cx="5" cy="5" r="4.2" fill="none" stroke="#e3222b" stroke-width="1.3"/><path d="M3 5l1.6 1.6L8 2.8" fill="none" stroke="#e3222b" stroke-width="1.4"/></svg><b>Solarenergie</b><span style="width:190px">sinnvoll geplant und fachgerecht umgesetzt</span></li>
  </ul>

  <div class="abs service-area"></div>
  <div class="abs packs">
    <h3>Servicepakete &amp; Wartung</h3>
    <p>Damit alles planbar bleibt und<br>Ausfälle reduziert werden:</p>
    <h4>Servicepakete &amp; Unterhalt nach Bedarf</h4>
    <p class="detail">(z.B. Armaturenservice/Reparaturen, Filterservice, Dachwartungsvertrag) – transparent, verlässlich, termintreu.</p>
  </div>

  <svg class="abs badge-ribbon" viewBox="0 0 176 28"><polygon points="0,0 164,0 176,28 0,28" fill="#e3222b"/></svg>
  <div class="abs badge-text">Sanitär-Notfallservice<br>und Kundendienst:</div>
  <div class="abs badge-circle">24<small>hr</small></div>

  <div class="abs footer-red">
    <div class="contact contact--phone" style="left:14px;top:2px">
      <svg width="8" height="8" viewBox="0 0 10 10"><circle cx="5" cy="5" r="5" fill="#fff"/><path d="M3 3l1.5 0 .5 1.5-1 .6a4 4 0 0 0 1.9 1.9l.6-1 1.5.5V8A5 5 0 0 1 3 3z" fill="#e3222b"/></svg>+41 41 555 20 40</div>
    <div class="contact" style="left:262px;top:5px">
      <svg width="7" height="7" viewBox="0 0 10 10"><circle cx="5" cy="5" r="5" fill="#fff"/><rect x="2.5" y="3.2" width="5" height="3.6" fill="#e3222b"/></svg>info@blindqvist-example.ch</div>
  </div>
  <div class="abs footer-navy">
    <div class="contact" style="left:14px;top:6px">
      <svg width="7" height="8" viewBox="0 0 10 12"><path d="M5 0a4.5 4.5 0 0 1 4.5 4.5C9.5 8 5 12 5 12S.5 8 .5 4.5A4.5 4.5 0 0 1 5 0z" fill="#fff"/><circle cx="5" cy="4.5" r="1.6" fill="#1f2f55"/></svg>Lindenweg 14, 4999 Musterdorf</div>
    <div class="contact" style="left:262px;top:6px">
      <svg width="7" height="7" viewBox="0 0 10 10"><circle cx="5" cy="5" r="4.3" fill="none" stroke="#fff" stroke-width="1.2"/><path d="M.7 5h8.6M5 .7c-2 2.5-2 6 0 8.6M5 .7c2 2.5 2 6 0 8.6" fill="none" stroke="#fff" stroke-width=".9"/></svg>www.blindqvist-example.ch</div>
  </div>
</section>

</body>
</html>
```